BrightHarbor.com Web Site Theme - Home Page/Front Page - Sub-Page theme

Looking for a new site theme that uses tiles like Quellingreport.com but with a unique style. Topbar categories should include following in any particular order w/ pop-out at touch w/ sub-categories (examples below): The main categories for display have an >> prefix . Note main catgories and sub-categories may change.

SPECIAL NOTE: Regional site. We need a way to navigate/drill-down to specific regions on the Central Coast (see the cities accross the top on the current site design)

PORTAL SITE: This site will have a back-end w/ my account and therefore may use a Bootstrap template on the back-end for managing Tiles and articles. Tiles would be the organic content/advertisements on the home page that link to the sub-pages.

TOP BAR CATEGORIES - click to open pop-up w/ sub-categories (some examples in Dining and Real Estate below)

>>Lodging

>>Dining (sub categories below)
Go to Dining >>
Bars & Nightclubs
Lunch & Dinner
Catering
Chinese
Coffee
Italian
Pizza
Seafood
Steakhouse
More >>

>>Wineries

>>Activities & Events

>>Real Estate

>>For Sale (subcategories below)
Auto
Shopping

>>Jobs
..

Target Market(s)

Hotels, Wineries, Restaurants, Tourists

Industry/Entity Type

Real Estate

Coding

Coded - Design and coding required

Number of Pages Required

3 page

Colors
0255a3

Requirements
Must have
• My account (maybe a black bar w/ BH logo accross top w/ My Account, Settings, Login etc)
• Conversion of existing organic content and advertisements to new Tiles platform.
Nice to have
• Kind of a Hybrid between Zorvik.com and QuellingReport.com
• PORTAL THOUGHTS
• If everything were to be thought of as a tile to preview in a 3 column wide format w/ variable heights you can fit articles and sound content mixed in with advertorials.
• Every square tile on BrightHarbor.com could be encapsulated into a “Tile”. The Tile is the preview of the landing page, article, or page.
• Every article, business listings, google map page, etc. can have a Tile associated with it. OR you create a Tile and link it to a URL/page.
• So Tiles become mini snippets of custom HTML that can have 1 or more links etc… Just an HTML Snippet.
• Tile/HTML Snippet
• PreviewTiles.aspx
• Shows all tiles sortable like a product catalog, etc. Additional columns for publishing the tile and where it should reside on the Front Page?
• NEW THEME
• Removal of the traditional BH sidebar and incorporating the triple tile site design. We can still have Tallowmere or a major display as first thing you see above top-bar. The categories can be incorporated into a simple top-bar that on-click you pop-down all subcategories and anything featured. This supports tablets and handhelds instead of the traditional mouse-over...
• Comp Layout (see quellingreport.com)
• 3 columns to 1 column style?
• How to handle mobile devices? (Tiles technique supports Plonko news mobile app - 3 columns PC/Mac browser - 1 column Mobile Phone
• Tile & Page MGT
• How do we convert the existing content pages to our new Tile/Page technique?
• How do we handle advertising Tiles and Tiles embedded on pages?
• Pages
• How is a page handled?
• How are Tiles managed and is that a Page or not?
• How are listings handled and are they defined as a Page?

```html
<!DOCTYPE html>
<html lang="en">
<head>
<meta charset="utf-8">
<title>BrightHarbor.com – Home</title>
<link href="https://fonts.googleapis.com/css2?family=Roboto:wght@400;500;700&family=Oswald:wght@400;500;600&display=swap" rel="stylesheet">
<style>
:root{
  --brand:#0255a3;
  --brand-bright:#1d6fc6;
  --brand-deep:#0a3f86;
  --nav-top:#2a7fd6;
  --nav-bottom:#135fb7;
  --accent-red:#d0202a;
  --ink:#333333;
  --ink-soft:#555555;
  --rule:#dddddd;
  --panel:#ededed;
  --wood:#262626;
  --wood-dark:#151515;
  --white:#ffffff;
}
*{box-sizing:border-box;margin:0;padding:0}
html,body{width:1200px;height:2233px;overflow:hidden;background:var(--white)}
body{font-family:"Roboto",Arial,sans-serif;color:var(--ink);position:relative}
.abs{position:absolute}
a{color:inherit;text-decoration:none}

/* utility bar */
.utility-bar{position:absolute;left:0;top:0;width:1200px;height:30px;background:var(--brand-bright);color:var(--white);font-size:11px}
.utility-bar span{position:absolute;top:9px}

/* header */
.site-header{position:absolute;left:0;top:30px;width:1200px;height:131px;background:linear-gradient(180deg,#2e2e2e,var(--wood-dark));}
.contact-phone{position:absolute;left:168px;top:46px;font-size:17px;color:#4a9be8;font-weight:500}
.contact-mail{position:absolute;left:168px;top:69px;font-size:12px;color:var(--white)}
.brand-name{position:absolute;left:600px;top:38px;transform:translateX(-50%);font-size:42px;font-weight:500;color:var(--white);letter-spacing:-0.5px;white-space:nowrap}
.search-box{position:absolute;left:831px;top:49px;width:235px;height:37px;background:var(--white);border:1px solid #ccc;font-size:11px;color:#999;padding:11px 10px}
.search-btn{position:absolute;left:1066px;top:49px;width:36px;height:37px;background:var(--brand-bright)}

/* main nav */
.main-nav{position:absolute;left:0;top:161px;width:1200px;height:50px;background:linear-gradient(180deg,var(--nav-top),var(--nav-bottom));}
.main-nav .item{position:absolute;top:19px;transform:translateX(-50%);font-size:11px;color:var(--white);letter-spacing:.3px;white-space:nowrap}
.main-nav .active{position:absolute;left:98px;top:0;width:136px;height:50px;background:var(--brand-deep)}
.dropdown{position:absolute;left:234px;top:222px;width:173px;background:var(--brand-bright);box-shadow:0 3px 8px rgba(0,0,0,.3);z-index:5}
.dropdown li{list-style:none;height:36.8px;line-height:36.8px;padding-left:24px;font-size:11px;color:var(--white);border-bottom:1px solid rgba(255,255,255,.18)}
.dropdown li:first-child{background:var(--brand-deep)}

/* hero */
.hero{position:absolute;left:0;top:211px;width:1200px;height:514px;background:linear-gradient(180deg,#5b8fd0 0%,#a9c6e6 38%,#c6d6dc 55%,#d9b06b 72%,#e2a451 100%)}
.hero-kicker{position:absolute;left:630px;top:400px;transform:translateX(-50%);font-family:"Oswald",sans-serif;font-weight:500;font-size:22px;color:var(--white);white-space:nowrap;text-shadow:0 1px 3px rgba(0,0,0,.4)}
.hero-title{position:absolute;left:630px;top:425px;transform:translateX(-50%);font-family:"Oswald",sans-serif;font-weight:600;font-size:40px;color:var(--white);white-space:nowrap;text-shadow:0 1px 4px rgba(0,0,0,.4)}
.hero-shadow{position:absolute;left:100px;top:725px;width:1000px;height:30px;background:radial-gradient(ellipse at top,rgba(0,0,0,.28),rgba(0,0,0,0) 70%)}

/* section headers */
.section-head{position:absolute;height:52px;background:var(--panel);border-left:3px solid var(--brand);font-size:15px;font-weight:500;color:var(--ink);padding:18px 0 0 17px;text-transform:uppercase}

/* tiles */
.photo{position:absolute}
.tile-title{position:absolute;font-size:15px;font-weight:500;color:var(--ink);line-height:20px}
.tile-text{position:absolute;font-size:11.5px;color:var(--ink-soft);line-height:20px}
.tag-row{position:absolute;height:34px;display:flex;font-size:11px}
.tag-row .tag{width:91px;background:var(--brand);color:var(--white);text-align:center;line-height:34px}
.tag-row .time{width:100px;border:1px solid var(--rule);line-height:32px;padding-left:5px;color:var(--ink)}
.read-more{position:absolute;font-size:11px;color:var(--ink);display:flex;align-items:center;gap:10px}
.read-more i{display:block;width:24px;height:20px;background:var(--brand)}
.meta{position:absolute;font-size:11px;color:var(--ink)}
.meta b{color:var(--accent-red);font-weight:500;margin-right:16px}
.list-title{position:absolute;font-size:14.5px;font-weight:500;color:var(--ink);line-height:20px}
.list-text{position:absolute;font-size:11.5px;color:var(--ink-soft);line-height:20px}
.outline-btn{position:absolute;height:33px;border:1px solid var(--rule);text-align:center;line-height:31px;font-size:11px;color:var(--ink)}

/* top posts */
.tabs{position:absolute;left:98px;top:1850px;width:654px;height:20px;border-bottom:1px solid var(--rule);font-size:11px}
.tabs span{margin-right:12px}
.tabs .on{border-bottom:3px solid var(--brand);padding-bottom:4px}
.carousel-arrow{position:absolute;width:28px;height:26px;background:rgba(0,0,0,.55)}

/* follow */
.follow-box{position:absolute;left:774px;top:1851px;width:328px;height:238px;background:var(--panel);border:1px solid #e3e3e3}
.follow-icons{position:absolute;left:0;top:0;width:326px;height:56px;background:var(--white)}
.follow-text{position:absolute;left:16px;top:75px;width:300px;font-size:11px;line-height:19px;color:var(--ink-soft)}
.email-field{position:absolute;left:14px;top:149px;width:198px;height:33px;background:var(--white);border:1px solid #ddd;font-size:11px;color:#999;padding:9px 10px}
.signup{position:absolute;left:227px;top:149px;width:92px;height:33px;background:var(--brand-deep);color:var(--white);font-size:12px;text-align:center;line-height:33px}
.newsletter{position:absolute;left:16px;top:199px;font-size:11px;display:flex;align-items:center;gap:8px}
.newsletter i{display:block;width:11px;height:11px;border:1px solid #888;background:var(--white)}

/* footer */
.site-footer{position:absolute;left:0;top:2111px;width:1200px;height:122px;background:linear-gradient(180deg,#2a2a2a,var(--wood-dark));color:var(--white);font-size:11px}
.site-footer .links{position:absolute;left:600px;top:60px;transform:translateX(-50%);white-space:nowrap}
.site-footer .copy{position:absolute;left:600px;top:88px;transform:translateX(-50%);white-space:nowrap}
.site-footer .base{position:absolute;left:0;bottom:0;width:1200px;height:5px;background:var(--brand)}
</style>
</head>
<body>

<div class="utility-bar">
  <span style="left:99px">Tech</span>
  <span style="left:134px">Entertainment</span>
  <span style="left:222px">Politics</span>
  <span style="left:269px">More</span>
  <span style="left:981px">Log in</span>
  <span style="left:1025px">|</span>
  <span style="left:1039px">My Account</span>
</div>

<header class="site-header">
  <svg class="abs" style="left:142px;top:48px" width="20" height="26" viewBox="0 0 20 26"><path d="M5 2 C2 4 1 9 3 14 C5 19 9 23 13 24 L16 20 L12 17 L10 19 C8 17 6 13 6 10 L9 9 L8 3 Z" fill="#4a9be8"/></svg>
  <div class="contact-phone">65 4210 7735</div>
  <div class="contact-mail">hello@brightharbor.net</div>
  <div class="brand-name">BrightHarbor.com</div>
  <div class="search-box">Enter your keyword...</div>
  <div class="search-btn">
    <svg width="36" height="37" viewBox="0 0 36 37"><circle cx="17" cy="17" r="5" fill="none" stroke="#fff" stroke-width="2"/><line x1="21" y1="21" x2="25" y2="25" stroke="#fff" stroke-width="2.4"/></svg>
  </div>
</header>

<nav class="main-nav">
  <div class="active"></div>
  <span class="item" style="left:168px">LODGING</span>
  <span class="item" style="left:304px">DINING</span>
  <span class="item" style="left:433px">WINERIES</span>
  <span class="item" style="left:601px">ACTIVITIES &amp; EVENTS</span>
  <span class="item" style="left:776px">REAL ESTATE</span>
  <span class="item" style="left:914px">FOR SALE</span>
  <span class="item" style="left:1034px">JOBS</span>
</nav>

<section class="hero" role="img" aria-label="Tropical beach with palm trees, colourful boats on the sand and blue sky"></section>
<div class="hero-kicker">BUSINESS AND ENTERTAINMENT</div>
<div class="hero-title">GUIDE FOR THE CALIFORNIA</div>
<svg class="abs" style="left:28px;top:450px" width="34" height="34" viewBox="0 0 34 34"><circle cx="17" cy="17" r="15" fill="rgba(255,255,255,.2)" stroke="#fff" stroke-width="2"/><path d="M20 10 L13 17 L20 24" fill="none" stroke="#fff" stroke-width="2.4"/></svg>
<svg class="abs" style="left:1125px;top:450px" width="34" height="34" viewBox="0 0 34 34"><circle cx="17" cy="17" r="15" fill="rgba(255,255,255,.2)" stroke="#fff" stroke-width="2"/><path d="M14 10 L21 17 L14 24" fill="none" stroke="#fff" stroke-width="2.4"/></svg>
<svg class="abs" style="left:565px;top:688px" width="50" height="12" viewBox="0 0 50 12"><circle cx="7" cy="6" r="5" fill="var(--brand)"/><circle cx="24" cy="6" r="5" fill="#fff"/><circle cx="41" cy="6" r="5" fill="#fff"/></svg>
<div class="hero-shadow"></div>

<ul class="dropdown">
  <li>BARS &amp; NIGHTCLUBS</li>
  <li>LUNCH &amp; DINNER</li>
  <li>CATERING</li>
  <li>CHINESE</li>
  <li>COFFEE</li>
  <li>ITALIAN</li>
  <li>PIZZA</li>
</ul>

<!-- Featured blog post -->
<div class="section-head" style="left:98px;top:768px;width:654px">Featured Blog Post</div>

<div class="photo" style="left:98px;top:838px;width:317px;height:225px;background:linear-gradient(180deg,#3f8fd6 0%,#7fc6e6 45%,#e8e0c8 100%)" role="img" aria-label="Family running on a tropical beach"></div>
<div class="tile-title" style="left:98px;top:1072px">Traveling California's Central Coast<br>5 Reasons to Move to the West Coast</div>
<div class="tag-row" style="left:98px;top:1127px"><span class="tag">WORLD</span><span class="time">10:11 PM, FEB 02</span></div>
<div class="tile-text" style="left:98px;top:1168px;width:310px">Your travel, business and entertainment guide for the California Central Coast! Located along the Pacific Ocean halfway between Los Angeles and artisan villages.</div>
<div class="read-more" style="left:98px;top:1240px"><i></i>READ MORE</div>

<div class="photo" style="left:432px;top:838px;width:318px;height:225px;background:linear-gradient(135deg,#1a3f73 0%,#4d7fb5 50%,#b9d2ea 100%)" role="img" aria-label="Viewers in 3D glasses on a sofa"></div>
<div class="tile-title" style="left:432px;top:1072px">Nuclear Fusion Closer to Becoming a Reality<br>entertainment</div>
<div class="tag-row" style="left:432px;top:1127px"><span class="tag">WORLD</span><span class="time">10:11 PM, FEB 02</span></div>
<div class="tile-text" style="left:432px;top:1168px;width:316px">Maecenas mauris elementum, est morbi interdum cursus at elite imperdiet libero. Proin odios dapibus integer an nulla augue pharetra cursus.</div>
<div class="read-more" style="left:432px;top:1240px"><i></i>READ MORE</div>

<!-- Recommended -->
<div class="section-head" style="left:774px;top:768px;width:328px">Recommended</div>
<div class="photo" style="left:774px;top:838px;width:328px;height:152px;background:radial-gradient(circle at 60% 30%,#d79a48 0%,#6b3a1c 45%,#2a140a 100%)" role="img" aria-label="Wine bottles with festive lights"></div>
<div class="list-title" style="left:774px;top:1001px">Fusion Closer to Becoming a Reality</div>
<div class="meta" style="left:774px;top:1027px"><b>WORLD</b>10:11 PM, FEB 02</div>
<div class="photo" style="left:774px;top:1060px;width:328px;height:152px;background:linear-gradient(180deg,#7fc1e8 0%,#37a6c8 50%,#efe9dc 100%)" role="img" aria-label="Couple walking on a white sand beach"></div>
<div class="list-title" style="left:774px;top:1222px">Nuclear Fusion Closer to Becoming a Reality</div>
<div class="meta" style="left:774px;top:1249px"><b>WORLD</b>10:11 PM, FEB 02</div>

<!-- Latest from entertainment -->
<div class="section-head" style="left:98px;top:1294px;width:654px">Latest From Entertainment</div>
<div class="photo" style="left:98px;top:1370px;width:317px;height:205px;background:radial-gradient(circle at 50% 40%,#b07a42 0%,#5a3418 50%,#24130a 100%)" role="img" aria-label="Wine bottles and filled glasses"></div>
<div class="tile-title" style="left:98px;top:1591px">Traveling California's Central Coast</div>
<div class="tag-row" style="left:98px;top:1618px"><span class="tag">WORLD</span><span class="time">10:11 PM, FEB 02</span></div>
<div class="tile-text" style="left:98px;top:1655px;width:310px">Your travel, business and entertainment guide for the California Central Coast! Located along the Pacific Ocean halfway between Los Angeles and artisan villages.</div>
<div class="read-more" style="left:98px;top:1727px"><i></i>READ MORE</div>

<div class="photo" style="left:432px;top:1371px;width:125px;height:102px;background:linear-gradient(160deg,#1b2f6a,#3d5fb0 60%,#0d1533)" role="img" aria-label="Singer performing on stage"></div>
<div class="list-title" style="left:568px;top:1367px">Elementom Closer to<br>Becoming a Reality</div>
<div class="list-text" style="left:568px;top:1410px">Maecenas mauris elementum,<br>est interdum cursus ...</div>
<div class="meta" style="left:568px;top:1457px"><b>WORLD</b>10:11 PM, FEB 02</div>

<div class="photo" style="left:432px;top:1486px;width:125px;height:102px;background:linear-gradient(160deg,#0f1f55,#2f63c0 55%,#6a4a2a)" role="img" aria-label="Guitarist on a lit stage"></div>
<div class="list-title" style="left:568px;top:1481px">Maecenas Closer to<br>Becoming a Reality</div>
<div class="list-text" style="left:568px;top:1524px">Maecenas mauris elementum,<br>est interdum cursus ...</div>
<div class="meta" style="left:568px;top:1571px"><b>WORLD</b>10:11 PM, FEB 02</div>

<div class="photo" style="left:432px;top:1602px;width:125px;height:102px;background:radial-gradient(circle at 60% 20%,#e1b27a,#6b4020 50%,#1b0f08)" role="img" aria-label="Concert crowd with raised hands"></div>
<div class="list-title" style="left:568px;top:1598px">Nuclear Fusion Closer to<br>Becoming a Reality</div>
<div class="list-text" style="left:568px;top:1641px">Maecenas mauris elementum,<br>est interdum cursus ...</div>
<div class="meta" style="left:568px;top:1688px"><b>WORLD</b>10:11 PM, FEB 02</div>

<div class="outline-btn" style="left:432px;top:1721px;width:318px">MORE FROM ENTERTAINMENT</div>

<!-- Latest posts -->
<div class="section-head" style="left:774px;top:1294px;width:328px">Latest Posts</div>
<div class="photo" style="left:774px;top:1371px;width:127px;height:102px;background:linear-gradient(135deg,#c9b59a,#8a2a2a 55%,#e9e2d6)" role="img" aria-label="Couple walking in a shopping street"></div>
<div class="list-title" style="left:911px;top:1367px">Fusion Closer to<br>Becoming a Reality</div>
<div class="list-text" style="left:911px;top:1410px">Maecenas mauris elementum,<br>est interdum cursus ...</div>
<div class="meta" style="left:911px;top:1457px"><b>WORLD</b>10:11 PM, FEB 02</div>

<div class="photo" style="left:774px;top:1486px;width:127px;height:102px;background:radial-gradient(circle at 50% 55%,#d9a93a,#b98220 40%,#f6f3ee 75%)" role="img" aria-label="Gold wedding rings"></div>
<div class="list-title" style="left:911px;top:1481px">Maecenas Closer to<br>Becoming a Reality</div>
<div class="list-text" style="left:911px;top:1524px">Maecenas mauris elementum,<br>est interdum cursus ...</div>
<div class="meta" style="left:911px;top:1571px"><b>WORLD</b>10:11 PM, FEB 02</div>

<div class="photo" style="left:774px;top:1602px;width:127px;height:102px;background:linear-gradient(160deg,#a7c94a,#4f8a2a 55%,#c6548a)" role="img" aria-label="Watering can over a flower bed"></div>
<div class="list-title" style="left:911px;top:1598px">Nuclear Fusion Closer to<br>Becoming a Reality</div>
<div class="list-text" style="left:911px;top:1641px">Maecenas mauris elementum,<br>est interdum cursus ...</div>
<div class="meta" style="left:911px;top:1688px"><b>WORLD</b>10:11 PM, FEB 02</div>

<div class="outline-btn" style="left:774px;top:1721px;width:328px">SHOW MORE</div>

<!-- Top posts -->
<div class="section-head" style="left:98px;top:1775px;width:654px">Top Posts</div>
<div class="tabs"><span class="on">Most Recent</span><span>Most Read</span><span>Most Commented</span></div>

<div class="photo" style="left:98px;top:1888px;width:200px;height:140px;background:linear-gradient(180deg,#9fb4d6 0%,#6d8fc0 40%,#2f5f9e 100%)" role="img" aria-label="Pier stretching over the ocean"></div>
<div class="carousel-arrow" style="left:98px;top:1998px"><svg width="28" height="26" viewBox="0 0 28 26"><path d="M17 8 L11 13 L17 18" fill="none" stroke="#fff" stroke-width="2.4"/></svg></div>
<div class="list-title" style="left:98px;top:2042px;font-size:15px">Travel on Brotherhood Club</div>
<div class="meta" style="left:98px;top:2068px"><b>WORLD</b>10:11 PM, FEB 02</div>

<div class="photo" style="left:322px;top:1888px;width:201px;height:140px;background:linear-gradient(135deg,#2f6f3a,#c93a3a 45%,#e8d34a 75%,#3a3a3a)" role="img" aria-label="Group of runners at a race"></div>
<div class="list-title" style="left:322px;top:2042px;font-size:15px">Built on Brotherhood Club</div>
<div class="meta" style="left:322px;top:2068px"><b>WORLD</b>10:11 PM, FEB 02</div>

<div class="photo" style="left:548px;top:1888px;width:201px;height:140px;background:linear-gradient(160deg,#e3e3e3,#6a6a6a 45%,#1f1f1f)" role="img" aria-label="Rows of wine bottles"></div>
<div class="carousel-arrow" style="left:721px;top:1998px"><svg width="28" height="26" viewBox="0 0 28 26"><path d="M11 8 L17 13 L11 18" fill="none" stroke="#fff" stroke-width="2.4"/></svg></div>
<div class="list-title" style="left:548px;top:2042px;font-size:15px">Central on Brotherhood Club</div>
<div class="meta" style="left:548px;top:2068px"><b>WORLD</b>10:11 PM, FEB 02</div>

<!-- Follow -->
<div class="section-head" style="left:774px;top:1775px;width:328px">Follow QuellingReport</div>
<div class="follow-box">
  <div class="follow-icons">
    <svg class="abs" style="left:44px;top:15px" width="240" height="26" viewBox="0 0 240 26">
      <rect x="0" y="0" width="26" height="26" fill="#d6d6d6"/>
      <path d="M4 7 H22 V19 H4 Z M4 7 L13 14 L22 7" fill="none" stroke="#888" stroke-width="1.4"/>
      <rect x="42" y="0" width="26" height="26" fill="#3b5a99"/>
      <rect x="84" y="0" width="26" height="26" fill="#2aa3d8"/>
      <rect x="125" y="0" width="26" height="26" fill="#c8402f"/>
      <rect x="167" y="0" width="26" height="26" fill="#e8751a"/>
      <rect x="209" y="0" width="26" height="26" fill="#111"/>
      <rect x="216" y="4" width="12" height="18" rx="2" fill="none" stroke="#fff" stroke-width="1.6"/>
    </svg>
  </div>
  <div class="follow-text">Your travel, business and entertainment guide for the California Central Coast! Located along the Pacific Ocean halfway between Los Angeles</div>
  <div class="email-field">Enter your email address</div>
  <div class="signup">Sign up</div>
  <div class="newsletter"><i></i>Newsletters</div>
</div>

<footer class="site-footer">
  <svg class="abs" style="left:517px;top:18px" width="166" height="32" viewBox="0 0 166 32">
    <g fill="none" stroke="#fff" stroke-width="1.4">
      <circle cx="16" cy="16" r="14"/><circle cx="50" cy="16" r="14"/><circle cx="83" cy="16" r="14"/><circle cx="116" cy="16" r="14"/><circle cx="150" cy="16" r="14"/>
    </g>
  </svg>
  <div class="links">Privacy Policy | &nbsp;&nbsp;Store Locator | &nbsp;&nbsp;Advanced Search | &nbsp;&nbsp;Terms &amp; Conditions</div>
  <div class="copy">Copyrights © 2015 brightharbor . All rights reserved.</div>
  <div class="base"></div>
</footer>

</body>
</html>
```